For our product portfolio we need a new packaging design. Our product is a Guaraná-derived energy in powder form. It is sold in small bags, between 350 x 400 mm and 700 x 800 mm, and also in boxes e.g. in the size of 240 x 160 x 45mm.

Our goal is to get creative product design which can be used for
a) the small bags,
b) the boxes, and
c) our Web site logo.

Target Market(s)

Our current target market are computer and Internet geeks. Therefore, we used a LOL-cat in our current/previous design. With the new design we would like to address a broader audience. It would be nice to see logos and packaging designs that are suitable to catch the attention of both geeks as well as normal folks.

Our target audience are people who would buy energy drinks or drink a lot of coffee.

The target audience are young people who work hard and/or go to parties and festivals. The design should be rather playful and funny than serious business.

Industry/Entity Type

Product

Requirements
Must have
• 1. A relationship to the nature product Guaraná. You could, for example, use the red fruits and green leaves of the guarana plant in the design to signal that the product is organic and good for your health. Take a look at http://en.plinthopedia.example/wiki/Guarana for inspirations.
• 2. Our product name is "Velora Fizzpulver"
• 3. The small bags must have certain information in multiple languages (please see image attached as file 1 for reference). We will tell you the specifics when your design is selected as one of our favorites. However, please keep some space in your packaging design for the information text.
• 4. The boxes must have certain information in multiple languages (please see image attached as file 3 for reference). We will tell you the specifics when your design is selected as one of our favorites.
• 5. The graphics must be delivered in an open format so that we can make changes and adjustments after the competition has finished.
• 6. The graphics for packaging must use CMYK colors with at least 600dpi. The logo must use RGB colors with 72dpi.
• Please avoid resemblance with other trademarks, such as Tovimba Borealis.
Nice to have
• A brand identity that is appealing to the "Internet community", e.g. a LOL-cat animal, an Internet meme, or the like.
• Another idea would be to use a hybrid animal, such as http://www.snipmorphs.example/gallery/data/418/medium/stretch_snipmorphs.jpg
• In any case, creative and imaginative submissions are preferred over boring submissions. We are open to all ideas.

```html
<!DOCTYPE html>
<html lang="de">
<head>
<meta charset="utf-8">
<title>Velora Fizzpulver – Box Cover</title>
<link href="https://fonts.googleapis.com/css2?family=Russo+One&family=PT+Serif:wght@700&display=swap" rel="stylesheet">
<style>
  :root {
    --page-bg: #ece4e2;
    --cover-bg: #c4fbfb;
    --blob: #93cfd0;
    --brand-red: #d8134f;
    --molecule-dark: #4a4a4a;
    --molecule-light: #9a9a9a;
    --molecule-fade: rgba(196, 251, 251, 0);
    --text-dark: #1b1b1b;
  }
  * { margin: 0; padding: 0; box-sizing: border-box; }
  html, body {
    width: 1200px;
    height: 927px;
    overflow: hidden;
    background: var(--page-bg);
  }
  .canvas {
    position: relative;
    width: 1200px;
    height: 927px;
    display: flex;
    align-items: center;
    justify-content: center;
  }
  .box-cover {
    position: relative;
    width: 780px;
    height: 520px;
    background: var(--cover-bg);
    overflow: hidden;
    box-shadow: 0 6px 18px rgba(0,0,0,0.18);
  }
  .box-cover__blobs {
    position: absolute;
    inset: 0;
    width: 100%;
    height: 100%;
  }
  .product-title {
    position: absolute;
    left: 70px;
    top: 60px;
    font-family: "Russo One", sans-serif;
    font-size: 40px;
    line-height: 1.2;
    letter-spacing: 1px;
    color: var(--brand-red);
  }
  .molecule {
    position: absolute;
    left: 220px;
    top: 125px;
    width: 300px;
    height: 180px;
    background: radial-gradient(ellipse closest-side at 50% 50%,
      var(--molecule-light) 0%,
      var(--molecule-dark) 60%,
      var(--molecule-fade) 100%);
  }
  .brand-mark {
    position: absolute;
    left: 220px;
    top: 204px;
    width: 300px;
    height: 22px;
    display: flex;
    align-items: center;
    justify-content: center;
    gap: 6px;
    font-family: "Russo One", sans-serif;
    font-size: 15px;
    line-height: 22px;
    color: var(--brand-red);
  }
  .brand-mark__dot {
    width: 12px;
    height: 12px;
    border-radius: 50%;
    background: var(--brand-red);
  }
  .warning-text {
    position: absolute;
    right: 60px;
    top: 315px;
    width: 320px;
    font-family: "PT Serif", serif;
    font-weight: 700;
    font-size: 13px;
    line-height: 1.3;
    text-align: right;
    color: var(--text-dark);
  }
</style>
</head>
<body>
<main class="canvas">
  <section class="box-cover">
    <svg class="box-cover__blobs" viewBox="0 0 780 520" aria-hidden="true">
      <path d="M560 0 C600 40 680 30 720 70 C760 110 780 100 780 90 L780 0 Z" fill="var(--blob)"/>
      <path d="M0 440 C60 420 110 380 170 360 C240 340 290 390 330 440 C360 480 380 520 380 520 L0 520 Z" fill="var(--blob)"/>
      <path d="M600 520 C620 470 680 440 730 450 C760 456 780 470 780 470 L780 520 Z" fill="var(--blob)"/>
      <line x1="20" y1="150" x2="50" y2="160" stroke="var(--blob)" stroke-width="3"/>
      <circle cx="56" cy="162" r="6" fill="var(--blob)"/>
    </svg>

    <h1 class="product-title">Velora Fizzpulver</h1>

    <div class="molecule" role="img" aria-label="Molekül-Illustration aus gepunkteten grauen Kugeln mit Verbindungslinien"></div>

    <div class="brand-mark">
      <span class="brand-mark__dot"></span>
      <span>Velora Fizzpulver</span>
    </div>

    <p class="warning-text">
      Enthält Guaraná<br>
      Erhöhter Koffeingehalt (2,5g Coffein/100g).<br>
      Nicht für Kinder, Schwangere und<br>
      Koffein-empfindliche Personen geeignet.
    </p>
  </section>
</main>
</body>
</html>
```